Escrow Accounting firm needs a website design for a startup that services clients nationally.

I offer escrow accounting services for title companies and real estate attorneys. I've enclosed a logo, color palette and flyers with content that can be used for the site.

I'm looking for a similar design concept as the website below from my former employer. Please don't copy because of copyright infringement. Including for design ideas only.
www.harborlinefiduciary.com

Below is a brief write-up...
For professionals in the title insurance industry, finding a trustworthy and budget-friendly solution for escrow accounting can be daunting. When choosing the right accounting partner, title companies and law firms need a group they can rely on, and that's where we come in.

```html
<!DOCTYPE html>
<html lang="en">
<head>
<meta charset="utf-8">
<title>Meridian Escrow Solutions – Escrow Accounting Services</title>
<link href="https://fonts.googleapis.com/css2?family=Montserrat:wght@600;700;800&family=Poppins:wght@300;400;500;600&display=swap" rel="stylesheet">
<style>
:root{
  --salmon:#b9725e;
  --salmon-dark:#9c5a48;
  --navy:#262e3b;
  --navy-soft:#323b4a;
  --ink:#1d232d;
  --text:#4d5460;
  --muted:#7b818b;
  --line:#d9d9dd;
  --paper:#ffffff;
  --mist:#f4f4f6;
}
*{margin:0;padding:0;box-sizing:border-box}
html,body{width:1200px;height:3309px;overflow:hidden}
body{position:relative;background:var(--paper);font-family:"Poppins",sans-serif;color:var(--text)}
.abs{position:absolute}
h1,h2,h3{font-family:"Montserrat",sans-serif;color:var(--ink)}

/* buttons */
.btn{position:absolute;display:flex;align-items:center;height:39px;color:#fff;font-family:"Poppins",sans-serif;font-weight:600;font-size:11px;letter-spacing:.2px;text-transform:uppercase;text-decoration:none;z-index:3;
  background:linear-gradient(115deg,var(--salmon) 0,var(--salmon) 70%,var(--salmon-dark) 70%)}
.btn .label{flex:1;text-align:center;padding-right:24px}
.btn .arrow{position:absolute;right:10px;top:50%;transform:translateY(-50%);width:18px;height:18px}
.btn.dark{background:linear-gradient(115deg,var(--navy) 0,var(--navy) 70%,var(--salmon) 70%);border:1px solid #fff}

/* header */
.brand{font-family:"Poppins",sans-serif;font-weight:600;color:var(--salmon);display:flex;align-items:center;gap:8px}
.brand .dot{width:14px;height:14px;background:var(--salmon);border-radius:50%}
.nav{left:597px;top:22px;display:flex;align-items:center;gap:0;font-size:12px;color:var(--ink)}
.nav a{color:var(--ink);text-decoration:none;padding:0 27px;border-right:1px solid #c9c9cf;line-height:12px}
.nav a:nth-child(4){border-right:0}
.nav .cta{background:var(--salmon);color:#fff;font-size:10px;padding:9px 17px;border:0;margin-left:4px}

/* hero */
.hero{left:0;top:0;width:1200px;height:565px;background:linear-gradient(90deg,#fff 0,#fff 28%,#f1eeec 55%,#d9d6d4 100%)}
.hero-photo{left:330px;top:0;width:870px;height:565px;background:radial-gradient(ellipse at 70% 45%,rgba(200,195,192,.55),rgba(255,255,255,0) 70%)}
.hero h1{left:161px;top:128px;font-size:50px;line-height:54px;font-weight:800;letter-spacing:.5px}
.hero h1 .accent{color:var(--salmon)}
.hero p{left:161px;top:300px;width:390px;font-size:12px;line-height:20px;color:var(--text)}

.features{left:216px;top:537px;width:768px;height:52px;background:#fff;box-shadow:0 6px 18px rgba(0,0,0,.12);display:flex;align-items:center;justify-content:space-around;font-size:11.5px;color:var(--ink);z-index:5}
.features div{display:flex;align-items:center;gap:12px;white-space:nowrap}

/* services */
.services{left:0;top:565px;width:1200px;height:497px;background:var(--navy)}
.section-title{font-size:30px;font-weight:700;text-align:center;width:1200px;left:0}
.card{top:716px;width:276px;height:264px;background:#fff;overflow:hidden;clip-path:polygon(14px 0,100% 0,100% 100%,0 100%,0 14px)}
.card h3{position:absolute;left:18px;top:30px;font-family:"Poppins",sans-serif;font-size:15px;font-weight:600;line-height:19px;color:var(--ink);z-index:2}
.card .photo{position:absolute;right:0;top:45px;width:175px;height:219px;clip-path:polygon(0 22%,100% 0,100% 100%,0 100%)}
.card .more{position:absolute;left:18px;top:204px;font-size:9px;color:var(--salmon);font-weight:500;display:flex;align-items:center;gap:3px}

/* about */
.about-photo{left:0;top:1090px;width:245px;height:339px;background:linear-gradient(180deg,#e8e4e1,#cfc8c3 55%,#3a3d43 56%,#22252b)}
.about h2{left:258px;top:1112px;font-size:30px;font-weight:700;color:var(--navy)}
.about .lead{left:258px;top:1158px;width:330px;font-size:11.5px;line-height:19px;font-weight:500;color:var(--ink)}
.about .body{left:258px;top:1266px;width:335px;font-size:11.5px;line-height:19.5px;color:var(--text)}
.about-side{left:626px;top:1062px;width:574px;height:367px;background:linear-gradient(180deg,#f3f4f6 0,#e3e6ea 60%,#a8b0ba 85%,#6c7480 100%)}
.about-side p{position:absolute;left:45px;top:95px;width:420px;font-size:11.5px;line-height:19px;font-weight:500;color:var(--ink)}

/* why choose */
.why h2{left:205px;top:1512px;font-size:30px;font-weight:700;color:#2d3440}
.row-num{left:205px;font-family:"Montserrat",sans-serif;font-size:18px;font-weight:600;color:var(--salmon)}
.row-title{left:332px;font-family:"Montserrat",sans-serif;font-size:18px;font-weight:600;color:var(--ink)}
.row-text{left:649px;width:390px;font-size:11px;line-height:19px;color:var(--text)}

/* cta */
.cta-box{left:114px;top:1966px;width:860px;height:197px;background:var(--navy);clip-path:polygon(0 0,100% 0,88% 100%,0 100%)}
.cta-box h2{position:absolute;left:51px;top:29px;font-size:30px;line-height:34px;font-weight:700;color:#fff}
.cta-box p{position:absolute;left:383px;top:46px;width:340px;font-size:11px;line-height:19px;color:#e5e6ea}

/* testimonials */
.quote{top:2306px;width:204px;height:232px;background:#fff;box-shadow:0 4px 18px rgba(0,0,0,.09);padding:22px 18px}
.quote .mark{font-family:"Montserrat",sans-serif;font-size:56px;font-weight:800;line-height:40px;color:var(--salmon);height:38px}
.quote p{margin-top:14px;font-size:10px;line-height:18.5px;color:var(--text)}
.quote .who{margin-top:8px;font-size:12px;color:var(--ink);display:flex;align-items:center;gap:8px}
.quote .who::before{content:"";width:24px;height:1px;background:var(--ink)}

/* contact */
.touch-band{left:0;top:2628px;width:1200px;height:286px;background:var(--salmon)}
.tower{left:55px;top:2610px;width:152px;height:304px;background:linear-gradient(90deg,#3e4654,#b9bcc2 45%,#e6e2dc 60%,#8e9098);clip-path:polygon(30% 0,70% 3%,100% 12%,100% 100%,0 100%,0 20%)}
.touch-band h2{position:absolute;left:249px;top:118px;font-size:30px;font-weight:700;color:#fff}
.touch-band p{position:absolute;left:249px;top:167px;width:340px;font-size:11px;line-height:19px;color:#fbe9e3}
.form{left:608px;top:2660px;width:441px;height:303px;background:#fff;box-shadow:0 6px 20px rgba(0,0,0,.1);z-index:4}
.field{position:absolute;height:38px;border:1px solid #cfd1d6;border-radius:3px}
.field.active{border-color:var(--ink)}
.field label{position:absolute;left:18px;top:-8px;background:#fff;padding:0 5px 0 5px;font-size:11px;color:var(--ink)}
.field span{position:absolute;left:23px;top:13px;font-size:11px;color:#9a9ea6}

/* footer */
.footer{left:0;top:2914px;width:1200px;height:395px;background:var(--navy)}
.footer .logo{position:absolute;left:100px;top:148px;font-size:24px}
.social{position:absolute;top:214px;display:flex;gap:8px;left:153px}
.social i{width:24px;height:24px;border-radius:50%;background:var(--navy-soft);display:block}
.vline{position:absolute;top:128px;width:1px;height:120px;background:#3d4554}
.fcol h4{position:absolute;font-family:"Poppins",sans-serif;font-size:14px;font-weight:600;color:#fff;padding-left:10px;border-left:2px solid var(--salmon);line-height:14px}
.flist{position:absolute;font-size:10.5px;line-height:22.5px;color:#d9dbe0}
.contact-line{position:absolute;display:flex;align-items:flex-start;gap:12px;font-size:10.5px;line-height:15px;color:#e1e3e8}
.contact-line svg{flex:none;margin-top:1px}
.sub{position:absolute;left:884px;top:3117px;width:213px;height:38px;background:#fff;display:flex;z-index:4}
.sub span{flex:1;font-size:9px;color:#9a9ea6;padding:13px 0 0 22px}
.sub b{width:45px;background:var(--salmon);display:flex;align-items:center;justify-content:center}
.footer .rule{position:absolute;left:87px;top:324px;width:1026px;height:1px;background:#3d4554}
.footer .legal{position:absolute;top:355px;font-size:9px;color:#e1e3e8}
</style>
</head>
<body>

<!-- hero -->
<section class="abs hero">
  <div class="abs hero-photo" role="img" aria-label="Soft background photo of a person at a laptop handing over house keys"></div>
  <div class="abs brand" style="left:161px;top:16px;font-size:17px"><i class="dot"></i>Meridian Escrow Solutions</div>
  <nav class="abs nav">
    <a>Home</a><a>About Us</a><a>Services</a><a>Reviews</a><a class="cta">CONTACT US</a>
  </nav>
  <h1 class="abs"><span class="accent">ESCROW<br>ACCOUNTING</span><br>SERVICES</h1>
  <p class="abs">Escrow accounting services are at the heart of what we do. Trust us to provide you with peace of mind. With Meridian Escrow Solutions, you can be confident.</p>
  <a class="btn" style="left:163px;top:392px;width:197px"><span class="label">GET STARTED NOW</span>
    <svg class="arrow" viewBox="0 0 18 18"><circle cx="9" cy="9" r="8" fill="none" stroke="#fff" stroke-width="1.2"/><path d="M5.5 9h7M9.5 6l3 3-3 3" fill="none" stroke="#fff" stroke-width="1.2"/></svg></a>
</section>

<!-- services -->
<section class="abs services"></section>

<div class="abs features">
  <div><svg width="30" height="30" viewBox="0 0 30 30" fill="none" stroke="#2d3440" stroke-width="1.3"><circle cx="15" cy="17" r="7"/><circle cx="15" cy="17" r="3" stroke="#b9725e"/><path d="M5 8l2-2M25 8l-2-2M15 3v4"/></svg>Professionals With Knowledge</div>
  <div><svg width="30" height="30" viewBox="0 0 30 30" fill="none" stroke="#2d3440" stroke-width="1.3"><circle cx="14" cy="15" r="10"/><circle cx="14" cy="15" r="6"/><circle cx="14" cy="15" r="2" stroke="#b9725e"/><path d="M14 15l11-9"/></svg>Compliance and Accuracy</div>
  <div><svg width="30" height="30" viewBox="0 0 30 30" fill="none" stroke="#2d3440" stroke-width="1.3"><circle cx="15" cy="11" r="7"/><path d="M4 24c4 3 18 3 22 0" stroke="#b9725e"/><path d="M9 20c3-4 9-4 12 0"/></svg>Providing Customer Service</div>
</div>

<h2 class="abs section-title" style="top:651px;color:#fff">OUR SERVICES</h2>
<article class="abs card" style="left:161px"><h3>Escrow<br>Reconciliation</h3><div class="photo" role="img" aria-label="Photo of two people shaking hands" style="background:linear-gradient(135deg,#efe9e6,#d9b7a6 60%,#c79a86)"></div><span class="more">LEARN MORE <svg width="11" height="11" viewBox="0 0 18 18"><circle cx="9" cy="9" r="8" fill="none" stroke="#b9725e" stroke-width="1.5"/><path d="M5.5 9h7M9.5 6l3 3-3 3" fill="none" stroke="#b9725e" stroke-width="1.5"/></svg></span></article>
<article class="abs card" style="left:463px"><h3>ALTA<br>Certification</h3><div class="photo" role="img" aria-label="Photo of a smiling professional in a mustard blazer reviewing documents" style="background:linear-gradient(135deg,#2c2a2d 0,#3d2f2a 40%,#d9a443 70%,#f2e3c6)"></div><span class="more">LEARN MORE <svg width="11" height="11" viewBox="0 0 18 18"><circle cx="9" cy="9" r="8" fill="none" stroke="#b9725e" stroke-width="1.5"/><path d="M5.5 9h7M9.5 6l3 3-3 3" fill="none" stroke="#b9725e" stroke-width="1.5"/></svg></span></article>
<article class="abs card" style="left:766px"><h3>Data Call<br>Services</h3><div class="photo" role="img" aria-label="Photo of a support agent with a headset at a laptop" style="background:linear-gradient(160deg,#eef0f2,#c9b5a4 45%,#3c4048 75%,#2a2d33)"></div><span class="more">LEARN MORE <svg width="11" height="11" viewBox="0 0 18 18"><circle cx="9" cy="9" r="8" fill="none" stroke="#b9725e" stroke-width="1.5"/><path d="M5.5 9h7M9.5 6l3 3-3 3" fill="none" stroke="#b9725e" stroke-width="1.5"/></svg></span></article>

<!-- about -->
<section class="about">
  <div class="abs about-photo" role="img" aria-label="Portrait photo of a businesswoman with folded arms"></div>
  <h2 class="abs">ABOUT US</h2>
  <p class="abs lead">Meridian Escrow Solutions has accounting experts who understand the title industry and the importance of compliance, security, and implementing precise escrow accounting procedures along with timely monthly reporting.</p>
  <p class="abs body">For professionals in the title insurance industry, finding a trustworthy and budget-friendly solution for escrow accounting can be daunting.  When choosing the right accounting partner, title companies and law firms need a group they can rely on, and that's where we come in.</p>
  <div class="abs about-side" role="img" aria-label="Misty city skyline photo">
    <p>Escrow accounting services are at the heart of what we do. Trust us to provide you with peace of mind. With Meridian Escrow Solutions, you can be confident that your escrow accounting will be secure, accurate, and in complete compliance with Underwriter Requirements and Best Practices.</p>
  </div>
  <a class="btn" style="left:671px;top:1272px;width:152px"><span class="label">LEARN MORE</span>
    <svg class="arrow" viewBox="0 0 18 18"><circle cx="9" cy="9" r="8" fill="none" stroke="#fff" stroke-width="1.2"/><path d="M5.5 9h7M9.5 6l3 3-3 3" fill="none" stroke="#fff" stroke-width="1.2"/></svg></a>
</section>

<!-- why choose -->
<section class="why">
  <h2 class="abs">WHY CHOOSE US?</h2>
  <a class="btn" style="left:815px;top:1512px;width:152px"><span class="label">LEARN MORE</span>
    <svg class="arrow" viewBox="0 0 18 18"><circle cx="9" cy="9" r="8" fill="none" stroke="#fff" stroke-width="1.2"/><path d="M5.5 9h7M9.5 6l3 3-3 3" fill="none" stroke="#fff" stroke-width="1.2"/></svg></a>
  <div class="abs row-num" style="top:1610px">01</div>
  <div class="abs row-title" style="top:1610px">Industry Expertise</div>
  <p class="abs row-text" style="top:1609px">Our team consists of seasoned professionals with deep knowledge of the title insurance and real estate industries. We understand the intricacies of escrow accounting and ensure your accounts are managed with the highest level of precision.</p>
  <div class="abs row-num" style="top:1722px">02</div>
  <div class="abs row-title" style="top:1722px">Compliance &amp; Accuracy</div>
  <p class="abs row-text" style="top:1721px">We stay updated on the latest regulatory requirements to ensure your escrow accounts are fully compliant with state and federal laws. Our attention to detail means you can trust us to handle your accounting needs without errors.</p>
  <div class="abs row-num" style="top:1833px">03</div>
  <div class="abs row-title" style="top:1833px">Customized Solutions</div>
  <p class="abs row-text" style="top:1832px">We recognize that every business is unique. That's why we offer tailored accounting services designed to fit the specific needs of your company, whether you're a large title firm or a small law office.</p>
</section>

<!-- cta -->
<div class="abs cta-box">
  <h2>CONTACT US FOR<br>A CUSTOM QUOTE</h2>
  <p>Discover How Our Expert Escrow Accounting Services Can Protect Your Business—Get a Free Consultation Today!</p>
</div>
<a class="btn" style="left:165px;top:2086px;width:167px"><span class="label">OUR SERVICES</span>
  <svg class="arrow" viewBox="0 0 18 18"><circle cx="9" cy="9" r="8" fill="none" stroke="#fff" stroke-width="1.2"/><path d="M5.5 9h7M9.5 6l3 3-3 3" fill="none" stroke="#fff" stroke-width="1.2"/></svg></a>
<a class="btn dark" style="left:341px;top:2086px;width:160px"><span class="label">GET IN TOUCH</span>
  <svg class="arrow" viewBox="0 0 18 18"><circle cx="9" cy="9" r="8" fill="none" stroke="#fff" stroke-width="1.2"/><path d="M5.5 9h7M9.5 6l3 3-3 3" fill="none" stroke="#fff" stroke-width="1.2"/></svg></a>

<!-- testimonials -->
<h2 class="abs section-title" style="top:2244px;color:#2d3440">SEE WHAT OUR CLIENTS THINK</h2>
<article class="abs quote" style="left:162px"><div class="mark">“</div><p>"Lorem Ipsum is simply dummy text of the printing and typesetting industry. Lorem Ipsum has been the industry's standard dummy text ever since the 1500s, when an unknown printer took a galley of type and scrambled.."</p><div class="who">Marcus Dell</div></article>
<article class="abs quote" style="left:388px"><div class="mark">“</div><p>"Lorem Ipsum is simply dummy text of the printing and typesetting industry. Lorem Ipsum has been the industry's standard dummy text ever since the 1500s, when an unknown printer took a galley of type and scrambled.."</p><div class="who">Lena Brooks</div></article>
<article class="abs quote" style="left:614px"><div class="mark">“</div><p>"Lorem Ipsum is simply dummy text of the printing and typesetting industry. Lorem Ipsum has been the industry's standard dummy text ever since the 1500s, when an unknown printer took a galley of type and scrambled.."</p><div class="who">Omar Reyes</div></article>
<article class="abs quote" style="left:836px"><div class="mark">“</div><p>"Lorem Ipsum is simply dummy text of the printing and typesetting industry. Lorem Ipsum has been the industry's standard dummy text ever since the 1500s, when an unknown printer took a galley of type and scrambled.."</p><div class="who">Nina Hale</div></article>

<!-- get in touch -->
<section class="abs touch-band">
  <h2>GET IN TOUCH</h2>
  <p>Let Us Handle the Complexities of Escrow Accounting So You Can Focus on Growing Your Business—Start with a Free Consultation!</p>
</section>
<div class="abs tower" role="img" aria-label="Photo of a twisting high-rise tower"></div>

<section class="abs footer">
  <div class="brand logo"><i class="dot"></i>Meridian Escrow Solutions</div>
  <div class="social"><i></i><i></i><i></i><i></i></div>
  <div class="vline" style="left:415px"></div>
  <div class="vline" style="left:593px"></div>
  <div class="vline" style="left:845px"></div>
  <div class="fcol">
    <h4 style="left:458px;top:136px">Quick Links</h4>
    <div class="flist" style="left:469px;top:166px">Home<br>About Us<br>Services<br>Contact Us</div>
    <h4 style="left:628px;top:136px">Contact Us</h4>
    <div class="contact-line" style="left:637px;top:170px"><svg width="11" height="11" viewBox="0 0 12 12"><path d="M2 1l2.5 0 1 3-1.5 1c.7 1.5 1.6 2.4 3 3l1-1.5 3 1V10c0 .6-.5 1-1 1C5 11 1 7 1 2c0-.5.4-1 1-1z" fill="#fff"/></svg>555-201-4830</div>
    <div class="contact-line" style="left:637px;top:204px"><svg width="11" height="11" viewBox="0 0 12 12"><rect x="1" y="2.5" width="10" height="7" fill="#fff"/><path d="M1 3l5 3.5L11 3" fill="none" stroke="#262e3b" stroke-width="1"/></svg><u>jlane@meridianescrow.com</u></div>
    <div class="contact-line" style="left:637px;top:236px"><svg width="11" height="13" viewBox="0 0 12 14"><path d="M6 13S1.5 8 1.5 5a4.5 4.5 0 019 0c0 3-4.5 8-4.5 8z" fill="#fff"/><circle cx="6" cy="5" r="1.6" fill="#262e3b"/></svg>120 Orchard Lane,<br>Fairview PA, 16400</div>
    <h4 style="left:884px;top:136px">Subscribe Newsletter</h4>
    <div class="flist" style="left:894px;top:160px;width:200px;line-height:15px">Subscribe newsletter for the latest offers and news</div>
  </div>
  <div class="rule"></div>
  <div class="legal" style="left:87px">Copyrights 2024. All Rights Reserved</div>
  <div class="legal" style="left:943px">Privacy Policy | Terms &amp; Conditions</div>
</section>
<div class="sub"><span>Enter Email...</span><b><svg width="16" height="8" viewBox="0 0 16 8"><path d="M0 4h14M11 1l3 3-3 3" fill="none" stroke="#fff" stroke-width="1.2"/></svg></b></div>

<form class="abs form">
  <div class="field active" style="left:19px;top:30px;width:195px"><label>First Name</label><span>Alexander</span></div>
  <div class="field" style="left:227px;top:30px;width:195px"><label>Last Name</label><span>What's your budget?</span></div>
  <div class="field" style="left:19px;top:93px;width:195px"><label>Email Adderess</label><span>Email Address</span></div>
  <div class="field" style="left:227px;top:93px;width:195px"><label>Number</label><span>Phone number</span></div>
  <div class="field" style="left:19px;top:153px;width:403px;height:72px"><label>Message</label><span style="top:8px">How can we help you?</span></div>
  <a class="btn" style="left:23px;top:246px;width:130px"><span class="label">SUBMIT</span>
    <svg class="arrow" viewBox="0 0 18 18"><circle cx="9" cy="9" r="8" fill="none" stroke="#fff" stroke-width="1.2"/><path d="M5.5 9h7M9.5 6l3 3-3 3" fill="none" stroke="#fff" stroke-width="1.2"/></svg></a>
</form>

</body>
</html>
```